Help a start up law firm make an impression! - Website

We are a property development and conveyancing law firm looking for some to design our website. The initial brief is for 6 pages with scope for on-going work.

Law firms are traditionally quite conservative and we want to break the mold. We want to come across as fun and modern, while still being professional.

A good example is https://quorvantlaw.com.au/. It's professional yet modern.
Updates

Another good site I like in the same industry: https://www.tamberwickconveyancing.com.au/

Target Market(s)

Tech savy home buyers and sellers - generally 30 to 50 years old

Industry/Entity Type

Law Firm

Coding

Coded - Design and coding required

Number of Pages Required

5+ page

Font styles to use
Other font styles liked:
• No idea

Colors
f04a50

Requirements
Must have
• The elements set out in the design brief document

```html
<!DOCTYPE html>
<html lang="en">
<head>
<meta charset="utf-8">
<title>Harrowby Law — The Property Law Experts</title>
<link rel="stylesheet" href="https://fonts.googleapis.com/css2?family=Source+Serif+4:wght@400;500;600;700&family=Source+Sans+3:wght@400;600&display=swap">
<style>
:root{
  --brand:#f04a50;
  --ink:#1d1d1d;
  --dark-panel:#202020;
  --card-grey:#f3f3f3;
  --muted:#555;
  --faint:#9a9a9a;
  --line:#d6d6d6;
  --white:#fff;
  --serif:"Source Serif 4", Georgia, serif;
  --sans:"Source Sans 3", Arial, sans-serif;
}
*{box-sizing:border-box;margin:0;padding:0}
html,body{width:1200px;height:2769px;overflow:hidden}
body{position:relative;background:var(--white);font-family:var(--sans);color:var(--ink)}
.abs{position:absolute}

/* header */
.site-header{left:0;top:0;width:1200px;height:83px;background:var(--white)}
.brand-name{left:98px;top:18px;font-family:var(--serif);font-weight:700;font-size:34px;color:var(--ink);letter-spacing:-.3px}
.call{left:838px;top:18px;display:flex;gap:14px;align-items:center}
.call-label{font-size:11.5px;text-transform:uppercase;color:#333;letter-spacing:.2px}
.call-number{font-size:25px;letter-spacing:1.4px;color:var(--ink);line-height:1}
.menu-toggle{left:1072px;top:28px}

/* hero */
.hero{left:0;top:83px;width:1200px;height:425px;background:linear-gradient(180deg,#2a3a6a 0%,#3d4f7e 45%,#4a4f62 62%,#1a2236 78%,#10131c 100%)}
.hero-title{left:0;top:280px;width:1200px;text-align:center;font-family:var(--serif);font-weight:600;font-size:34px;line-height:44px;color:var(--white);text-transform:uppercase;letter-spacing:.3px}
.hero-sub{left:0;top:325px;width:1200px;text-align:center;font-size:17.5px;line-height:24px;color:var(--white)}
.hero-btn{left:528px;top:373px;width:144px;height:38px;border:2px solid var(--brand);color:var(--white);font-family:var(--serif);font-size:16px;display:flex;align-items:center;justify-content:center}
.hero-arrow{top:295px}

/* features */
.feature{top:465px;width:236px;height:295px;background:var(--card-grey)}
.feature-head{height:61px;background:var(--brand);color:var(--white);font-family:var(--serif);font-size:15.5px;text-transform:uppercase;display:flex;align-items:center;justify-content:center;letter-spacing:.2px}
.feature-icon{width:72px;height:72px;border:1.5px solid var(--brand);border-radius:50%;margin:20px auto 0;display:flex;align-items:center;justify-content:center;background:var(--white)}
.feature-text{margin:18px 22px 0;font-size:11.5px;line-height:20px;color:#444;text-align:justify;text-align-last:center}

/* service bubbles */
.photo{background:#888}
.bubble-text{color:var(--white)}
.bubble-title{font-family:var(--serif);font-weight:600;font-size:30px;letter-spacing:.2px}
.bubble-copy{margin-top:18px;font-size:13px;line-height:26px;text-align:justify}
.btn-outline{display:inline-flex;align-items:center;justify-content:center;width:144px;height:38px;font-family:var(--serif);font-weight:600;font-size:16px}
.service-dark .btn-outline{border:2px solid var(--brand);color:var(--white)}
.service-red .btn-outline{border:2px solid var(--white);color:var(--white)}

/* blog */
.blog-heading{left:0;top:1626px;width:1200px;text-align:center;font-family:var(--serif);font-weight:600;font-size:30px}
.post{top:1684px;width:316px;height:463px;background:var(--white);box-shadow:0 2px 4px rgba(0,0,0,.18)}
.post-img{height:190px}
.post-title{margin:16px 24px 0;text-align:center;font-family:var(--serif);font-weight:500;font-size:17.5px;line-height:27px;color:var(--ink)}
.post-excerpt{margin:16px 24px 0;text-align:center;font-size:11.5px;line-height:26px;color:#555}
.post-meta{margin-top:16px;text-align:center;font-size:9.5px;color:var(--faint)}
.post-meta span{margin:0 8px}
.post-btn{position:absolute;left:92px;top:403px;width:130px;height:34px;border:2px solid var(--brand);color:var(--brand);font-family:var(--serif);font-weight:600;font-size:16px;display:flex;align-items:center;justify-content:center}

/* contact */
.contact{left:0;top:2197px;width:1200px;height:443px;background:radial-gradient(ellipse at 50% 55%,#dcdcdc 0%,#e6e6e6 45%,#efefef 100%)}
.contact-heading{left:0;top:2232px;width:1200px;text-align:center;font-family:var(--serif);font-weight:400;font-size:29px;color:#222}
.field{border:1px solid #cfcfcf;background:rgba(255,255,255,.35);font-size:12.5px;color:#333;padding:10px 14px}
.submit{left:535px;top:2531px;width:128px;height:35px;border:2px solid var(--brand);color:var(--brand);font-family:var(--serif);font-size:16px;display:flex;align-items:center;justify-content:center}
.social{left:545px;top:2598px;display:flex;gap:16px}
.social-link{display:block;width:11px;height:11px;border:1.5px solid #333;border-radius:2px}

/* footer */
.footer-brand{left:98px;top:2664px;font-family:var(--serif);font-weight:700;font-size:33px;color:var(--ink)}
.footer-nav{left:505px;top:2674px;display:flex;gap:25px;font-size:12.5px;color:#222}
.copyright{left:804px;top:2720px;font-size:11.5px;color:#444}
</style>
</head>
<body>

<header class="abs site-header">
  <div class="abs brand-name">Harrowby Law</div>
  <div class="abs call">
    <svg width="14" height="24" viewBox="0 0 14 24"><rect x="1" y="1" width="12" height="22" rx="2" fill="none" stroke="#222" stroke-width="2"/><rect x="3" y="4" width="8" height="13" fill="#222"/><circle cx="7" cy="20" r="1.2" fill="#fff"/></svg>
    <div>
      <div class="call-label">Call our experts today</div>
      <div class="call-number">1.800.314.2750</div>
    </div>
  </div>
  <svg class="abs menu-toggle" width="28" height="22" viewBox="0 0 28 22"><g stroke="#444" stroke-width="2"><line x1="0" y1="2" x2="28" y2="2"/><line x1="0" y1="11" x2="28" y2="11"/><line x1="0" y1="20" x2="28" y2="20"/></g></svg>
</header>

<section class="abs hero" role="img" aria-label="Photo of a city skyline at dusk with towers reflected in a river"></section>
<h1 class="abs hero-title">The Property Law Experts</h1>
<p class="abs hero-sub">Unrivaled response times, fixed fee options and experienced property lawyers</p>
<div class="abs hero-btn">Contact Us</div>
<svg class="abs hero-arrow" style="left:112px" width="10" height="14" viewBox="0 0 10 14"><path d="M8 1 2 7l6 6" fill="none" stroke="#fff" stroke-width="2"/></svg>
<svg class="abs hero-arrow" style="left:1078px" width="10" height="14" viewBox="0 0 10 14"><path d="M2 1l6 6-6 6" fill="none" stroke="#fff" stroke-width="2"/></svg>

<div class="abs feature" style="left:98px">
  <div class="feature-head">Cost Certainty</div>
  <div class="feature-icon"><svg width="40" height="40" viewBox="0 0 40 40"><text x="20" y="31" text-anchor="middle" font-family="Source Sans 3, sans-serif" font-size="34" fill="#222">$</text></svg></div>
  <p class="feature-text">Flexible fee arrangements with no surprises. We offer fixed fee, pay on completion and monthly retainer options to suit your needs.</p>
</div>
<div class="abs feature" style="left:354px">
  <div class="feature-head">Expert Lawyers</div>
  <div class="feature-icon"><svg width="40" height="40" viewBox="0 0 40 40"><circle cx="20" cy="13" r="8" fill="#222"/><path d="M5 37c0-9 7-14 15-14s15 5 15 14z" fill="#222"/><path d="M20 24l-2 4 2 8 2-8z" fill="var(--brand)"/></svg></div>
  <p class="feature-text">Our experienced team has managed over 2,000 conveyances and worked on some of the most iconic developments in Queensland. All we do is property law, all day everyday.</p>
</div>
<div class="abs feature" style="left:611px">
  <div class="feature-head">Responsive Service</div>
  <div class="feature-icon"><svg width="44" height="40" viewBox="0 0 44 40"><g fill="none" stroke="#222" stroke-width="2"><line x1="22" y1="4" x2="22" y2="34"/><line x1="6" y1="9" x2="38" y2="9"/><path d="M6 9 1 22h10z"/><path d="M38 9l-5 13h10z"/><path d="M1 22a5 4 0 0 0 10 0M33 22a5 4 0 0 0 10 0"/><line x1="13" y1="35" x2="31" y2="35"/></g></svg></div>
  <p class="feature-text">The most responsive service, guaranteed. No more waiting days for a lawyer to respond to your email, return your call or prepare your contract.</p>
</div>
<div class="abs feature" style="left:866px">
  <div class="feature-head">Commercial Advice</div>
  <div class="feature-icon"><svg width="40" height="40" viewBox="0 0 40 40"><g fill="#222"><rect x="13" y="15" width="14" height="14" rx="1"/><rect x="10" y="31" width="20" height="5"/><rect x="17" y="4" width="14" height="5" transform="rotate(-35 24 6)"/></g></svg></div>
  <p class="feature-text">We work with you to get the deal done without legal jargon getting in the way. We understand timing is crucial and we focus on the legal issues that are important to you.</p>
</div>

<!-- conveyancing -->
<div class="abs photo" style="left:98px;top:801px;width:511px;height:380px;background:linear-gradient(120deg,#d9dde2 0%,#9aa3ad 40%,#5b6068 70%,#c9b9aa 100%)" role="img" aria-label="Photo of a hand holding a glowing shield icon with a tick"></div>
<section class="service-dark">
  <svg class="abs" style="left:480px;top:826px;overflow:visible" width="614" height="370" viewBox="0 0 614 370">
    <defs><filter id="shadowDark" x="-10%" y="-10%" width="120%" height="130%"><feDropShadow dx="0" dy="6" stdDeviation="8" flood-opacity=".3"/></filter></defs>
    <path d="M95 8H588Q604 8 604 24V317Q604 333 588 333H95Q79 333 79 317V318L18 355L79 152V24Q79 8 95 8Z" fill="var(--dark-panel)" stroke="#fff" stroke-width="7" stroke-linejoin="round" filter="url(#shadowDark)"/>
  </svg>
  <div class="abs bubble-text" style="left:634px;top:858px;width:392px">
    <h2 class="bubble-title">Conveyancing Services</h2>
    <p class="bubble-copy">Sed ut perspiciatis unde omnis iste natus error sit voluptatem accusantium doloremque laudantium, totam rem aperiam, eaque ipsa quae ab illo inventore veritatis et quasi architecto beatae vitae dicta sunt explicabo. Nemo enim ipsam voluptatem quia voluptas sit aspernatur aut odit aut fugit, sed quia consequuntur magni dolores eos qui ratione voluptatem sequi nesciunt.</p>
    <div style="margin-top:20px"><span class="btn-outline">Read more</span></div>
  </div>
</section>

<!-- development -->
<div class="abs photo" style="left:585px;top:1207px;width:515px;height:381px;background:linear-gradient(160deg,#5f7489 0%,#3a4a5c 45%,#1e2632 100%)" role="img" aria-label="Photo of two business people exchanging documents against a city view"></div>
<section class="service-red">
  <svg class="abs" style="left:117px;top:1223px;overflow:visible" width="660" height="345" viewBox="0 0 660 345">
    <defs><filter id="shadowRed" x="-10%" y="-10%" width="120%" height="130%"><feDropShadow dx="0" dy="6" stdDeviation="8" flood-opacity=".3"/></filter></defs>
    <path d="M24 8H519Q535 8 535 24V180L636 296L535 305V317Q535 333 519 333H24Q8 333 8 317V24Q8 8 24 8Z" fill="var(--brand)" stroke="#fff" stroke-width="7" stroke-linejoin="round" filter="url(#shadowRed)"/>
  </svg>
  <div class="abs bubble-text" style="left:197px;top:1262px;width:392px">
    <h2 class="bubble-title">Development law services</h2>
    <p class="bubble-copy" style="margin-top:12px">Sed ut perspiciatis unde omnis iste natus error sit voluptatem accusantium doloremque laudantium, totam rem aperiam, eaque ipsa quae ab illo inventore veritatis et quasi architecto beatae vitae dicta sunt explicabo. Nemo enim ipsam voluptatem quia voluptas sit aspernatur aut odit aut fugit, sed quia consequuntur magni dolores eos qui ratione voluptatem sequi nesciunt.</p>
    <div style="margin-top:14px"><span class="btn-outline">Read more</span></div>
  </div>
</section>

<!-- blog -->
<h2 class="abs blog-heading">Blog</h2>
<article class="abs post" style="left:98px">
  <div class="post-img" style="background:linear-gradient(135deg,#c9d3dc,#6e7f8e 60%,#3b4450)" role="img" aria-label="Photo of a man working at computers in an office"></div>
  <h3 class="post-title">Lorem ipsum dolor sit amet, consectetur adipiscing elit.</h3>
  <p class="post-excerpt">Donec suscipit, enim et venenatis sollicitudin, sapien libero consectetur ligula, ac commodo odio tellus non massa.</p>
  <p class="post-meta"><span>Maren Holt</span>/<span>21 May 2017</span>/<span>2 Comments</span></p>
  <div class="post-btn">Read more</div>
</article>
<article class="abs post" style="left:439px">
  <div class="post-img" style="background:linear-gradient(135deg,#b9bfc4,#7a7d80 50%,#2e3033)" role="img" aria-label="Photo of two colleagues shaking hands in an office"></div>
  <h3 class="post-title">Lorem ipsum dolor sit amet, consectetur adipiscing elit.</h3>
  <p class="post-excerpt">Donec suscipit, enim et venenatis sollicitudin, sapien libero consectetur ligula, ac commodo odio tellus non massa.</p>
  <p class="post-meta"><span>Maren Holt</span>/<span>21 May 2017</span>/<span>2 Comments</span></p>
  <div class="post-btn">Read more</div>
</article>
<article class="abs post" style="left:783px">
  <div class="post-img" style="background:linear-gradient(135deg,#e4e4e2,#a7a9aa 50%,#4a4c4f)" role="img" aria-label="Photo of people working at desks in an open-plan office"></div>
  <h3 class="post-title">Lorem ipsum dolor sit amet, consectetur adipiscing elit.</h3>
  <p class="post-excerpt">Donec suscipit, enim et venenatis sollicitudin, sapien libero consectetur ligula, ac commodo odio tellus non massa.</p>
  <p class="post-meta"><span>Maren Holt</span>/<span>21 May 2017</span>/<span>2 Comments</span></p>
  <div class="post-btn">Read more</div>
</article>

<!-- contact -->
<section class="abs contact" role="img" aria-label="Faded photo of a team meeting around a table"></section>
<h2 class="abs contact-heading">Get In Touch</h2>
<div class="abs field" style="left:268px;top:2302px;width:317px;height:40px">First Name</div>
<div class="abs field" style="left:609px;top:2302px;width:320px;height:40px">Last Name</div>
<div class="abs field" style="left:268px;top:2354px;width:317px;height:40px">Email</div>
<div class="abs field" style="left:609px;top:2354px;width:320px;height:40px">Phone</div>
<div class="abs field" style="left:268px;top:2407px;width:661px;height:96px">Message</div>
<div class="abs submit">Get in touch</div>
<div class="abs social" aria-label="Social links"><span class="social-link"></span><span class="social-link"></span><span class="social-link"></span><span class="social-link"></span></div>

<!-- footer -->
<footer>
  <div class="abs footer-brand">Harrowby Law</div>
  <nav class="abs footer-nav"><span>Home</span><span>Conveyancing</span><span>Property Development</span><span>News &amp; Knowledge</span><span>About us</span><span>Contact Us</span></nav>
  <p class="abs copyright">© 2017. All rights reserved.&nbsp; | &nbsp;www.companyname.com</p>
</footer>

</body>
</html>
```